Contest - label design for a health related product with 4 color variations

Nuvera-Store (http://www.nuvera-store.example) is an online shop selling health related products and nutritional supplements, such as algae products, wheat grass and barley grass powder. These products have a positive impact on a person's health. Through Craft Huddle, we have designed already a logo for the shop and now we need to create labels that will be placed on a brown glass bottle (see attachment). The logo shall be used without the slogan 'Nuvera-Store' when creating the label.

Your job is to design a label with 4 color variations, blue, green, red and yellow. The measurements of the label is 80 mm x 173 mm, but please add 3 mm bleed to each side.

The information that has to go on the label can be taken from the attachment 'label information.pdf'. For the sake of communication, we will divide the label into 3 parts

- left
- middle
- right

The left part and the right part are fixed as this contains legal information. Please use easy to read fonts, non-serifed fonts, such as Arial, Verdana, Calibri. The left part contains a table and if Illustrator provides the possibility for tables, please use it as we need to be able to easily add and remove rows of the table.

The middle part contains the product description, the product quantity (i.e. 100 g), our logo without the slogan 'One live. Live it healthy.' and logos indicating the organic quality of the product (please see attachments). For the product name (i.e. QUB-Tangen) and the quantity (i.e. 100 Tabletten, 200 g) use the attached Lato font. Please note that the vertical position of our logo, the product name and the organic logos has NOT been set yet. You are free to position them where ever you feel in the middle part of the label.

Target Market(s)

Health concious people between 25 and 70

Industry/Entity Type

Health

Requirements
Must have
• - the attached logo without the slogan "One life...."
- the following attributes: healthy, joyful, vivid, lively, abstract, minimalistic
- colors that go along with our logo and the website www.nuvera-store.example
- all fonts need to be editable and not rendered
- the left part should have an editable table where we can add rows if necessary
- the attached font for product name and quantity
- 3 mm bleed on each side, so the final design is 6 mm wider and higher
- the final design will be in editable Illustrator files of a recent version.
Should not have
• - many overlaying, confusing lines or layers
- dark colors
- heavy appearance

```html
<!DOCTYPE html>
<html lang="de">
<head>
<meta charset="utf-8">
<title>QUB-Tangen Etikett</title>
<link href="https://fonts.googleapis.com/css2?family=Lato:wght@400;700;900&family=Arimo:wght@400;700&display=swap" rel="stylesheet">
<style>
  :root{
    --green-deep:#1f7a34;
    --green:#2e9a3e;
    --green-light:#6cc24a;
    --text:#1e1e1e;
    --white:#ffffff;
    --grey-edge:#d9dcd9;
    --badge:#7cc246;
  }
  *{margin:0;padding:0;box-sizing:border-box}
  html,body{width:1200px;height:566px;overflow:hidden;background:var(--white)}
  .label{position:relative;width:1200px;height:566px;overflow:hidden;font-family:"Arimo",Arial,sans-serif;color:var(--text)}
  .label-shapes{position:absolute;inset:0}
  .panel-left{position:absolute;left:16px;top:58px;width:290px;font-size:12.5px;line-height:1.35}
  .panel-left h3{font-size:12.5px;font-weight:700;margin-bottom:4px}
  .panel-left p{margin-bottom:16px}
  .nutrition{border-collapse:collapse;font-size:12.5px;margin-bottom:16px}
  .nutrition th{font-weight:700;text-align:left;padding:0 16px 4px 0}
  .nutrition td{padding:0 16px 1px 0}
  .vendor{line-height:1.35}
  .vendor strong{display:block}
  .panel-middle{position:absolute;left:330px;width:520px;top:0;text-align:center}
  .product-name{font-family:"Lato",sans-serif;font-weight:900;color:var(--green);font-size:44px;margin-top:60px;letter-spacing:.5px}
  .product-qty{font-family:"Lato",sans-serif;color:var(--green-deep);font-size:15px;margin-top:2px}
  .brand-mark{position:absolute;left:196px;top:170px;width:128px;height:128px}
  .brand-name{position:absolute;left:0;right:0;top:300px;font-family:"Lato",sans-serif;font-weight:700;color:var(--green-deep);font-size:34px}
  .badge{position:absolute;top:420px;height:56px}
  .badge-round{left:192px;width:56px;border-radius:50%;background:var(--white);border:3px solid var(--green-deep)}
  .badge-leaf{left:262px;width:80px;background:var(--badge)}
  .panel-right{position:absolute;left:908px;top:30px;width:280px;color:var(--white);font-size:12.5px;line-height:1.38}
  .panel-right h3{font-size:12.5px;font-weight:700;margin-bottom:12px}
  .panel-right p{margin-bottom:18px}
  .panel-right ul{list-style:none;margin-bottom:22px}
  .panel-right li{margin-bottom:1px}
</style>
</head>
<body>
<div class="label">
  <svg class="label-shapes" width="1200" height="566" viewBox="0 0 1200 566" aria-hidden="true">
    <defs>
      <linearGradient id="rightGrad" x1="0" y1="0" x2="1" y2="1">
        <stop offset="0" stop-color="#2f9c3f"/>
        <stop offset="1" stop-color="#1c6f2f"/>
      </linearGradient>
      <linearGradient id="swooshGrad" x1="0" y1="0" x2="1" y2="0">
        <stop offset="0" stop-color="#7cc246"/>
        <stop offset="1" stop-color="#2a8f3a"/>
      </linearGradient>
    </defs>
    <path d="M308 0 C322 180 318 400 308 566" fill="none" stroke="var(--grey-edge)" stroke-width="10"/>
    <path d="M314 566 C520 520 720 500 900 470 L900 566 Z" fill="url(#swooshGrad)"/>
    <path d="M330 566 C520 540 700 520 880 500" fill="none" stroke="#b7e08c" stroke-width="4"/>
    <path d="M870 0 L1200 0 L1200 566 L860 566 C850 400 880 200 870 0 Z" fill="url(#rightGrad)"/>
    <path d="M850 0 C862 200 838 400 852 566" fill="none" stroke="#8fd05a" stroke-width="5"/>
  </svg>

  <section class="panel-left">
    <h3>Zutaten</h3>
    <p>QUB-Tangen (AFA - Aphanizomenon Flos Aqua) aus dem Klamath Lake, bei 37° Celsius getrocknet.</p>
    <table class="nutrition">
      <tr><th>Nährwertangaben</th><th>in 100 g</th><th>pro Kapsel</th></tr>
      <tr><td>Kohlenhydrate</td><td></td><td></td></tr>
      <tr><td>Fett</td><td></td><td></td></tr>
      <tr><td>Eiweiß</td><td></td><td></td></tr>
      <tr><td>Brennwert (kJ / kcal)</td><td></td><td></td></tr>
    </table>
    <table class="nutrition">
      <tr><th>Inhaltsstoffe</th><th>pro Kapsel</th><th>% RDA</th></tr>
      <tr><td>Vitamin C</td><td>50,2 mg</td><td>50 %</td></tr>
    </table>
    <div class="vendor">
      <strong>Vertrieb</strong>
      Merrow Fenwick Limited<br>
      Lindenhof-Gasse 14<br>
      1220 Wien<br>
      Österreich
    </div>
  </section>

  <section class="panel-middle">
    <h1 class="product-name">QUB-Tangen</h1>
    <div class="product-qty">100 Tabletten, 200 g</div>
    <svg class="brand-mark" viewBox="0 0 128 128" aria-hidden="true">
      <circle cx="64" cy="64" r="58" fill="var(--green-light)"/>
    </svg>
    <div class="brand-name">Nuvera-Store</div>
    <div class="badge badge-round" role="img" aria-label="Bio-Prüfzeichen"></div>
    <div class="badge badge-leaf" role="img" aria-label="EU-Bio-Siegel"></div>
  </section>

  <section class="panel-right">
    <h3>Verzehrempfehlung</h3>
    <p>3 x täglich 3 – 5 Tabletten unzerkaut mit Wasser zu den Mahlzeiten einnehmen.</p>
    <h3>Hinweise</h3>
    <ul>
      <li>- Die angegebene tägliche Verzehrmenge sollte nicht überschritten werden.</li>
      <li>- Nahrungsergänzungsmittel sind kein Ersatz für eine ausgewogene und abwechslungsreiche Ernährung.</li>
      <li>- Das Produkt lichtgeschützt, verschlossen und außerhalb der Reichweite von kleinen Kindern aufbewahren.</li>
      <li>- Während der Schwangerschaft und Stillzeiten sollte vor dem Verzehr von Nahrungsergänzungsmitteln ein Arzt konsultiert werden.</li>
    </ul>
    <h3 style="margin-bottom:0">Mindesthaltbarkeitsdatum</h3>
    <div>Siehe Boden.</div>
  </section>
</div>
</body>
</html>
```